Lira Vantell Music Flyer for Social Media

The flyer needs to include the networks Lira Vantell music is distributed on such as TuneHarbor, WaveCastFM, Brook, and Sonorill. This flyer will be posted on social media websites such as friendloop, Pictogrove, and Chirpnet. The flyer will also be listed on the music artist official website. The artist logo is attached for additional creative ideas.

Target Market(s)

Music lovers

Industry/Entity Type

Music Download

Requirements
Must have
• Must have the music networks listed on the photo and the artist name.
Nice to have
• It would be nice to have the website listed: www.liravantell.example and artist logo.
Should not have
• Anything that is not listed in the project description.

```html
<!DOCTYPE html>
<html lang="en">
<head>
<meta charset="utf-8">
<title>Lira Vantell – Quiet Ember EP Flyer</title>
<link href="https://fonts.googleapis.com/css2?family=Roboto+Condensed:ital,wght@0,700;1,700;1,800&family=Open+Sans:wght@300;400;700&family=Great+Vibes&display=swap" rel="stylesheet">
<style>
  :root {
    --pink: #e8266f;
    --red: #d7202c;
    --navy: #2d2a83;
    --ink: #1b1b1b;
    --paper: #efedea;
    --bar-a: #1a4fa0;
    --bar-b: #0f6fbd;
    --white: #ffffff;
  }
  * { margin: 0; padding: 0; box-sizing: border-box; }
  html, body { width: 941px; height: 1200px; overflow: hidden; background: var(--paper); }
  .flyer { position: relative; width: 941px; height: 1200px; overflow: hidden; font-family: "Open Sans", sans-serif; }
  .portrait { position: absolute; left: 0; top: 0; width: 941px; height: 900px;
    background: radial-gradient(ellipse at 62% 42%, #6b4a3a 0%, #2c2b2c 32%, #16262c 60%, #0e1518 100%); }
  .waves { position: absolute; left: 0; top: 0; }
  .ep-title { position: absolute; right: 71px; top: 44px; text-align: right;
    font-family: "Roboto Condensed", sans-serif; font-weight: 700; font-size: 72px; line-height: 76px; color: var(--pink); }
  .brand-badge { position: absolute; left: 62px; top: 36px; width: 307px; height: 302px; border-radius: 50%;
    background: var(--white); border: 15px solid var(--pink);
    display: flex; flex-direction: column; align-items: center; justify-content: center; gap: 18px; }
  .brand-badge .name { font-weight: 400; font-size: 26px; letter-spacing: 6px; color: var(--ink); text-transform: uppercase; text-align: center; }
  .brand-badge .site { font-family: "Roboto Condensed", sans-serif; font-weight: 700; font-style: italic; font-size: 24px; color: var(--pink); }
  .bio { position: absolute; left: 52px; top: 382px; width: 311px; color: var(--white);
    font-weight: 300; font-size: 16.5px; line-height: 30px; text-align: justify; text-align-last: center; }
  .role-badge { position: absolute; left: 555px; top: 632px; width: 304px; height: 304px; border-radius: 50%;
    background: var(--pink); box-shadow: 0 4px 10px rgba(0,0,0,.25);
    display: flex; align-items: center; justify-content: center; }
  .role-badge p { font-family: "Roboto Condensed", sans-serif; font-weight: 800; font-style: italic; font-size: 58px; line-height: 60px; color: var(--white); }
  .artist-name { position: absolute; left: 45px; top: 984px; font-family: "Roboto Condensed", sans-serif; font-weight: 700; font-size: 56px; line-height: 62px; color: var(--pink); text-transform: uppercase; }
  .tagline { position: absolute; left: 48px; top: 1062px; font-family: "Great Vibes", cursive; font-size: 40px; color: var(--ink); }
  .website { position: absolute; left: 443px; top: 1000px; font-family: "Roboto Condensed", sans-serif; font-weight: 700; font-style: italic; font-size: 24px; color: var(--navy); }
  .socials { position: absolute; left: 720px; top: 994px; width: 190px; display: grid; grid-template-columns: 1fr 1fr; gap: 6px 8px; list-style: none; }
  .socials li { display: flex; align-items: center; gap: 5px; font-size: 12px; font-weight: 700; color: var(--navy); }
  .socials li::before { content: ""; width: 9px; height: 9px; border-radius: 50%; background: var(--navy); }
  .networks { position: absolute; left: 431px; top: 1082px; width: 465px; display: flex; justify-content: space-between; list-style: none; }
  .networks li { display: flex; align-items: center; gap: 6px; font-weight: 700; font-size: 18px; color: var(--ink); }
  .networks li::before { content: ""; width: 14px; height: 14px; border-radius: 50%; background: var(--ink); }
  .release-bar { position: absolute; left: 45px; top: 1136px; width: 851px; height: 38px;
    background: linear-gradient(90deg, var(--bar-a), var(--bar-b));
    display: flex; align-items: center; padding: 0 12px; gap: 10px; color: var(--white); white-space: nowrap; }
  .release-bar .track { font-family: "Roboto Condensed", sans-serif; font-weight: 800; font-size: 27px; letter-spacing: -0.5px; }
  .release-bar .track span { color: var(--pink); font-size: 20px; }
  .release-bar .credit { font-size: 14px; font-weight: 400; }
  .release-bar .pitch { margin-left: auto; font-family: "Roboto Condensed", sans-serif; font-weight: 700; font-style: italic; font-size: 20px; }
</style>
</head>
<body>
<main class="flyer">
  <div class="portrait" role="img" aria-label="Portrait photograph of the artist with long dark curly hair against a dark teal background"></div>

  <svg class="waves" width="941" height="1200" viewBox="0 0 941 1200" aria-hidden="true">
    <defs>
      <linearGradient id="redband" x1="0" x2="1">
        <stop offset="0" stop-color="#e8266f"/><stop offset="0.6" stop-color="#d7202c"/><stop offset="1" stop-color="#a8161e"/>
      </linearGradient>
    </defs>
    <path d="M941,360 C900,560 760,760 520,905 L941,905 Z" fill="#b4b5b8"/>
    <path d="M941,480 C880,650 760,800 560,900 L941,900 Z" fill="#e8266f"/>
    <path d="M941,560 C860,720 730,840 560,905 L941,905 Z" fill="#a8161e"/>
    <path d="M941,640 C850,780 720,870 560,910 L941,910 Z" fill="#8e8f93"/>
    <path d="M0,730 C180,800 380,830 620,828 L620,850 C380,850 160,820 0,770 Z" fill="#c9cacd"/>
    <path d="M0,770 C170,820 380,845 620,845 L620,880 C380,880 160,850 0,810 Z" fill="#e8266f"/>
    <path d="M0,810 C170,850 380,872 620,870 L620,890 C380,895 160,875 0,840 Z" fill="#1c1c1e"/>
    <path d="M0,840 C200,880 420,898 700,870 L941,790 L941,830 C700,920 420,920 0,880 Z" fill="url(#redband)"/>
    <path d="M0,880 C300,925 620,925 941,830 L941,1200 L0,1200 Z" fill="#c6c7ca"/>
    <path d="M0,895 C300,940 620,940 941,845 L941,1200 L0,1200 Z" fill="var(--paper)"/>
  </svg>

  <h1 class="ep-title">Quiet<br>Ember EP</h1>

  <div class="brand-badge">
    <span class="name">Lira<br>Vantell</span>
    <span class="site">liravantell.example</span>
  </div>

  <p class="bio">Maren Tolliske born March 14, 1993 is an American singer and songwriter. Raised in Millbrook, SC she first entered the music industry by recording demo tapes in 2013. The independent artist released her EP "Quiet Ember" in 2016, and it is globally distributed worldwide. Lira Vantell graduated from Northfield Central High School, and she is currently attending Eastvale State University to further her education.</p>

  <div class="role-badge"><p>SINGER<br>&amp; SONG<br>WRITER</p></div>

  <h2 class="artist-name">Lira Vantell</h2>
  <p class="tagline">Singer and Song Writer</p>

  <p class="website">www.liravantell.example</p>
  <ul class="socials">
    <li>friendloop</li>
    <li>Chirpnet</li>
    <li>Pictogrove</li>
    <li>ClipStream</li>
  </ul>

  <ul class="networks">
    <li>WaveCastFM</li>
    <li>TuneHarbor</li>
    <li>Sonorill</li>
    <li>Brook</li>
  </ul>

  <div class="release-bar">
    <span class="track">GLOW <span>(REMIX)</span></span>
    <span class="credit">by Lira Vantell: Released 2016</span>
    <span class="pitch">IT IS FULL OF ENERGY AND EXCITEMENT</span>
  </div>
</main>
</body>
</html>
```